Veterinary Business cards

Redesign Business Card

Information needed on Card:
Hours: Mon-Fri: 4pm -10PM; Sat- Sun- 10 AM- 5PM
Help@bayfernvet.com
www.bayfernvet.com
555-718-2946
4173 SE 19th Ave. okc, ok 73958
*No appointment necessary*

Optional:
Our tag line is "We're here when you need us" - If it fits on the cards.

```html
<!DOCTYPE html>
<html lang="en">
<head>
<meta charset="utf-8">
<title>Bayfern Vet Urgent Care – Business Card</title>
<link href="https://fonts.googleapis.com/css2?family=Marcellus&family=Questrial&family=Lato:wght@700&display=swap" rel="stylesheet">
<style>
  :root {
    --navy: #173c68;
    --navy-soft: #1f4777;
    --orange: #d9781f;
    --white: #ffffff;
    --paw-grey: #ececec;
    --stage: #e4e5e7;
  }
  * { box-sizing: border-box; margin: 0; padding: 0; }
  html, body { width: 1200px; height: 900px; overflow: hidden; }
  body {
    background: var(--stage);
    display: flex;
    flex-direction: column;
    align-items: center;
    justify-content: center;
    gap: 56px;
  }
  .card {
    position: relative;
    width: 620px;
    height: 354px;
    overflow: hidden;
    box-shadow: 0 6px 18px rgba(0,0,0,0.18);
  }
  .paw-area { position: absolute; border-radius: 50%; }

  /* Front side */
  .card-front { background: var(--navy); color: var(--white); }
  .card-front .paw-area { background: var(--navy-soft); }
  .front-brand {
    position: absolute; left: 0; right: 0; top: 112px;
    text-align: center;
  }
  .brand-name {
    font-family: "Marcellus", serif;
    letter-spacing: 2px;
    line-height: 1;
  }
  .card-front .brand-name { font-size: 52px; color: var(--white); }
  .brand-rule {
    margin: 14px auto 0;
    width: 400px; height: 2px; background: var(--white);
  }
  .brand-sub {
    font-family: "Marcellus", serif;
    font-size: 22px; letter-spacing: 5px;
    margin-top: 10px;
  }
  .card-front .brand-sub { color: var(--white); }
  .tagline {
    margin-top: 22px;
    font-family: "Questrial", sans-serif;
    font-size: 14px; letter-spacing: 2px;
  }

  /* Back side */
  .card-back { background: var(--white); color: var(--navy); }
  .card-back .paw-area.faint { background: var(--paw-grey); }
  .back-brand {
    position: absolute; left: 40px; top: 120px; width: 250px;
    text-align: center;
  }
  .card-back .brand-name { font-size: 38px; color: var(--navy); }
  .card-back .brand-rule { width: 240px; background: var(--navy); margin-top: 10px; }
  .card-back .brand-sub { font-size: 15px; color: var(--navy); letter-spacing: 4px; }

  .details { position: absolute; left: 330px; top: 56px; }
  .hours-title {
    font-family: "Lato", sans-serif; font-weight: 700;
    color: var(--orange); font-size: 18px; letter-spacing: 0.5px;
  }
  .hours-row { font-family: "Questrial", sans-serif; font-size: 14px; margin-top: 4px; }
  .hours-row b { font-family: "Lato", sans-serif; font-weight: 700; }
  .contact-list { list-style: none; margin-top: 22px; }
  .contact-list li {
    display: flex; align-items: center; gap: 8px;
    font-family: "Questrial", sans-serif; font-size: 15px;
    margin-bottom: 5px;
  }
  .icon { width: 14px; height: 14px; flex: none; }

  .notice-band {
    position: absolute; left: 0; right: 0; bottom: 30px; height: 40px;
    background: var(--navy); color: var(--white);
    font-family: "Marcellus", serif; font-size: 17px; letter-spacing: 1px;
    display: flex; align-items: center; padding-left: 140px;
  }
  .card-back .paw-area.accent { background: var(--orange); border: 3px solid var(--white); }
</style>
</head>
<body>

<section class="card card-front">
  <div class="paw-area" style="left:40px;top:70px;width:50px;height:50px" role="img" aria-label="faint paw print decoration"></div>
  <div class="paw-area" style="left:110px;top:50px;width:90px;height:90px" role="img" aria-label="faint paw print decoration"></div>
  <div class="paw-area" style="left:60px;top:170px;width:50px;height:50px" role="img" aria-label="faint paw print decoration"></div>
  <div class="paw-area" style="left:520px;top:120px;width:80px;height:80px" role="img" aria-label="faint paw print decoration"></div>
  <div class="paw-area" style="left:470px;top:210px;width:44px;height:44px" role="img" aria-label="faint paw print decoration"></div>

  <div class="front-brand">
    <div class="brand-name">BAYFERN VET</div>
    <div class="brand-rule"></div>
    <div class="brand-sub">URGENT CARE</div>
    <div class="tagline">WE'RE HERE WHEN YOU NEED US</div>
  </div>
</section>

<section class="card card-back">
  <div class="paw-area faint" style="left:20px;top:14px;width:44px;height:44px" role="img" aria-label="faint paw print decoration"></div>
  <div class="paw-area faint" style="left:76px;top:34px;width:80px;height:80px" role="img" aria-label="faint paw print decoration"></div>

  <div class="back-brand">
    <div class="brand-name">BAYFERN VET</div>
    <div class="brand-rule"></div>
    <div class="brand-sub">URGENT CARE</div>
  </div>

  <div class="details">
    <div class="hours-title">HOURS:</div>
    <div class="hours-row"><b>MON - FRI</b> - 4PM - 10PM</div>
    <div class="hours-row"><b>SAT- SUN</b> - 10 AM - 5PM</div>
    <ul class="contact-list">
      <li>
        <svg class="icon" viewBox="0 0 14 14" aria-hidden="true"><circle cx="7" cy="7" r="7" fill="var(--orange)"/><path d="M4.5 3.5l1.5 0 .6 1.8-.9.7a5 5 0 0 0 2.3 2.3l.7-.9 1.8.6v1.5c-3.5.3-6.3-2.5-6-6z" fill="#fff"/></svg>
        555-718-2946
      </li>
      <li>
        <svg class="icon" viewBox="0 0 14 14" aria-hidden="true"><circle cx="7" cy="7" r="7" fill="var(--orange)"/><rect x="3.5" y="4.5" width="7" height="5" fill="none" stroke="#fff" stroke-width="1"/><path d="M3.5 4.5l3.5 3 3.5-3" fill="none" stroke="#fff" stroke-width="1"/></svg>
        Help@bayfernvet.com
      </li>
      <li>
        <svg class="icon" viewBox="0 0 14 14" aria-hidden="true"><circle cx="7" cy="7" r="7" fill="var(--orange)"/><circle cx="7" cy="7" r="3.8" fill="none" stroke="#fff" stroke-width="0.9"/><path d="M3.2 7h7.6M7 3.2v7.6" stroke="#fff" stroke-width="0.9"/></svg>
        www.bayfernvet.com
      </li>
      <li>
        <svg class="icon" viewBox="0 0 14 14" aria-hidden="true"><circle cx="7" cy="7" r="7" fill="var(--orange)"/><path d="M3.5 7.2L7 4l3.5 3.2V10H3.5z" fill="#fff"/></svg>
        4173 SE 19th Ave. okc, ok 73958
      </li>
    </ul>
  </div>

  <div class="notice-band">*NO APPOINTMENT NECESSARY*</div>
  <div class="paw-area accent" style="left:500px;top:232px;width:44px;height:44px" role="img" aria-label="orange paw print decoration"></div>
  <div class="paw-area accent" style="left:540px;top:262px;width:70px;height:70px" role="img" aria-label="orange paw print decoration"></div>
</section>

</body>
</html>
```